Email Signature

Our company is having its 10th anniversary in 2021. We would like a new email signature to celebrate the occasion. Attached is our business card design.
Please refer to our website for actual contact details.
www.tarvinestates.com.au

Industry/Entity Type

Real Estate

Requirements
Must have
• Our logo
Email
Contact Numbers
Address
Website address

Celebrating 10 years in 2021
Nice to have
• Something that blends the designs of our website and business card

```html
<!DOCTYPE html>
<html lang="en">
<head>
<meta charset="utf-8">
<title>Tarvin Estates – Email Signature</title>
<link href="https://fonts.googleapis.com/css2?family=Exo+2:wght@700&family=Open+Sans:wght@400;700&display=swap" rel="stylesheet">
<style>
  :root {
    --backdrop: #4a4a4a;
    --card: #fbfbfb;
    --brand-blue: #1b5ea8;
    --ink: #1d1d1d;
    --text: #2b2b2b;
    --white: #ffffff;
    --seal-light: #e8bf45;
    --seal-deep: #c8951f;
  }
  * { margin: 0; padding: 0; box-sizing: border-box; }
  html, body { width: 1200px; height: 960px; overflow: hidden; }
  body { background: var(--backdrop); position: relative; font-family: "Open Sans", Arial, sans-serif; }

  .signature {
    position: absolute; left: 116px; top: 324px;
    width: 968px; height: 312px;
    background: var(--card); overflow: hidden;
  }
  .signature__name {
    position: absolute; left: 56px; top: 52px;
    font-family: "Exo 2", Arial, sans-serif; font-weight: 700;
    font-size: 22px; letter-spacing: 1.6px; color: var(--brand-blue);
  }
  .signature__role { position: absolute; left: 56px; top: 78px; font-size: 16px; color: var(--text); }
  .signature__rule {
    position: absolute; left: 56px; top: 118px;
    width: 708px; height: 2px; background: var(--brand-blue);
  }
  .brand-name {
    position: absolute; left: 692px; top: 125px;
    font-family: "Open Sans", Arial, sans-serif; font-weight: 700;
    font-size: 28px; color: var(--ink); letter-spacing: 0.5px;
  }

  .contact-list { position: absolute; left: 56px; top: 140px; list-style: none; }
  .contact-list li {
    display: flex; align-items: center; height: 21.5px;
    font-size: 16.5px; color: var(--text);
  }
  .contact-list svg { width: 14px; height: 14px; margin-right: 9px; fill: var(--brand-blue); flex: none; }

  .social-links { position: absolute; left: 337px; top: 145px; display: flex; gap: 6px; }
  .social-links span { width: 21px; height: 21px; border-radius: 50%; background: var(--brand-blue); }

  .address { position: absolute; left: 336px; top: 184px; display: flex; font-size: 16.5px; font-style: normal; color: var(--text); line-height: 21.5px; }
  .address svg { width: 14px; height: 18px; fill: var(--brand-blue); margin: 12px 8px 0 0; flex: none; }

  .footer-band { position: absolute; left: 0; top: 0; width: 968px; height: 312px; }
  .footer-band__message {
    position: absolute; right: 175px; top: 267px;
    font-size: 17px; color: var(--white);
  }
  .footer-band__message strong { font-weight: 700; }
  .anniversary-seal {
    position: absolute; left: 820px; top: 202px;
    width: 100px; height: 100px; border-radius: 50%;
    background: radial-gradient(circle at 40% 35%, var(--seal-light), var(--seal-deep));
  }
</style>
</head>
<body>
  <section class="signature">
    <svg class="footer-band" viewBox="0 0 968 312" aria-hidden="true">
      <polygon points="0,293 835,229 0,308" fill="var(--ink)"/>
      <polygon points="0,312 0,310 968,214 968,312" fill="var(--brand-blue)"/>
    </svg>

    <h1 class="signature__name">DANIEL K, MARLOWE</h1>
    <p class="signature__role">Owner</p>
    <div class="signature__rule"></div>
    <div class="brand-name">TARVIN ESTATES</div>

    <ul class="contact-list">
      <li><svg viewBox="0 0 14 14"><path d="M4 0h6a1 1 0 0 1 1 1v12a1 1 0 0 1-1 1H4a1 1 0 0 1-1-1V1a1 1 0 0 1 1-1zm0.5 1.5v10h5v-10z"/></svg>1300 00TARV (8278)</li>
      <li><svg viewBox="0 0 14 14"><path d="M3 1l2 3-1.3 1.3a8 8 0 0 0 4.9 4.9L10 9l3 2-1.2 2C6.5 13 1 7.5 1 2.2z"/></svg>8021 4390</li>
      <li><svg viewBox="0 0 14 14"><path d="M1 3h12v8H1zM1 3l6 4.5L13 3" stroke="var(--card)" stroke-width="1"/></svg>admin@tarvinestates.com.au</li>
      <li><svg viewBox="0 0 14 14"><circle cx="7" cy="7" r="6"/><path d="M1 7h12M7 1c-3 3-3 9 0 12M7 1c3 3 3 9 0 12" stroke="var(--card)" stroke-width="1" fill="none"/></svg>www.tarvinestates.com.au</li>
    </ul>

    <div class="social-links" aria-label="Social links"><span></span><span></span><span></span><span></span></div>

    <address class="address">
      <svg viewBox="0 0 14 18"><path d="M7 0a6 6 0 0 1 6 6c0 4.5-6 12-6 12S1 10.5 1 6a6 6 0 0 1 6-6zm0 3.5a2.5 2.5 0 1 0 0 5 2.5 2.5 0 0 0 0-5z"/></svg>
      <span>Shop 7/18 Harbourview Drive<br>Wentworth, NSW 2145</span>
    </address>

    <p class="footer-band__message">Celebrating <strong>10 YEARS</strong> in 2021</p>

    <div class="anniversary-seal" role="img" aria-label="Tenth anniversary seal"></div>
  </section>
</body>
</html>
```